Brightbay Business Card Design

Our company is called Brightbay. We manufacture confectionary snacks & frozen novelties. Our initial product portfolio includes frozen ice lollies/popsicles & stick ice cream bars.

We require a business card design.

Please use the attached Logo.

Please use an orange, brown, yellow colour code. You may choose any combination of the 3 or include all three. The logo however must remain orange.

Target Market(s)

Business card will be targeted at distributors of our products such as supermarket procurement managers, convenience store owners, wholesale distributors and merchandising agents.

Industry/Entity Type

Business

Requirements
Must have
• Calvin Obeng_Director/ P.O.Box Dunmore 5172, Accra, Ghana / m: 00233(0)507318924/ e: calvin.obeng@mailvora.co.uk

```html
<!DOCTYPE html>
<html lang="en">
<head>
<meta charset="utf-8">
<title>Brightbay Business Card</title>
<link rel="stylesheet" href="https://fonts.googleapis.com/css2?family=Roboto+Slab:wght@400;700&display=swap">
<style>
  :root {
    --page-bg: #d9d9d9;
    --brand-orange: #e8681e;
    --brand-brown: #5a3412;
    --card-white: #ffffff;
    --divider: rgba(255, 255, 255, 0.55);
    --text-font: "Roboto Slab", Georgia, serif;
  }

  html, body {
    margin: 0;
    padding: 0;
    width: 1200px;
    height: 900px;
    overflow: hidden;
    background: var(--page-bg);
    font-family: var(--text-font);
  }

  .sheet {
    position: relative;
    width: 1200px;
    height: 900px;
  }

  .card {
    position: absolute;
    left: 280px;
    width: 640px;
    height: 366px;
    box-sizing: border-box;
    box-shadow: 0 6px 18px rgba(0, 0, 0, 0.18);
  }

  /* Front */
  .card-front {
    top: 48px;
    background: var(--brand-orange);
    color: var(--card-white);
    display: flex;
    align-items: center;
  }

  .front-brand {
    width: 256px;
    display: flex;
    align-items: center;
    justify-content: center;
    gap: 9px;
  }

  .brand-dot {
    width: 26px;
    height: 26px;
    border-radius: 50%;
    background: var(--card-white);
    flex: none;
  }

  .brand-name {
    font-family: var(--text-font);
    font-weight: 700;
    font-size: 30px;
    line-height: 1;
    color: var(--card-white);
  }

  .front-divider {
    width: 2px;
    height: 250px;
    background: var(--divider);
    flex: none;
  }

  .contact {
    padding-left: 36px;
    font-size: 14.5px;
    line-height: 1.32;
  }

  .contact-name {
    margin: 0;
    font-size: 21px;
    font-weight: 700;
    line-height: 1.2;
  }

  .contact-role {
    margin: 0 0 18px;
    font-size: 15px;
  }

  .contact-details {
    margin: 0;
    font-style: normal;
  }

  /* Back */
  .card-back {
    top: 486px;
    background: var(--brand-brown);
  }

  .back-oval {
    position: absolute;
    left: 95px;
    top: 24px;
    width: 450px;
    height: 318px;
    border-radius: 50%;
    background: var(--card-white);
    display: flex;
    align-items: center;
    justify-content: center;
    gap: 14px;
  }

  .back-oval .brand-dot {
    width: 44px;
    height: 44px;
    background: var(--brand-orange);
  }

  .back-oval .brand-name {
    font-size: 56px;
    color: var(--brand-orange);
  }
</style>
</head>
<body>
  <main class="sheet">
    <section class="card card-front" aria-label="Business card front">
      <div class="front-brand">
        <span class="brand-dot"></span>
        <span class="brand-name">Brightbay</span>
      </div>
      <div class="front-divider"></div>
      <div class="contact">
        <p class="contact-name">Calvin Obeng</p>
        <p class="contact-role">Director</p>
        <address class="contact-details">
          P.O.Box Dunmore 5172,<br>
          Accra, Ghana<br>
          m: 00233(0)507318924<br>
          e: calvin.obeng@mailvora.co.uk
        </address>
      </div>
    </section>

    <section class="card card-back" aria-label="Business card back">
      <div class="back-oval">
        <span class="brand-dot"></span>
        <span class="brand-name">Brightbay</span>
      </div>
    </section>
  </main>
</body>
</html>
```